Kelto Mobile Apps Needs banners for webpage

We need a top banner. We are a mobile app developer for the Hospitality Industry. We are developing a Loyalty Program with the trade name KeltoPerks. The banner will be used on our loyalty page inside our website.Please see www.keltomobileapps-example.com to understand our theme. The banner should be 1700 X 470.

Please see the attached banner. This is from a competitor website.Please use it as a model and make changes...... make it unique to KeltoMobile. I need to convey the same message as this banner. Same statistics. Same setting (restaurant).

I have added a purchased vector file for the restaurant setting. I noticed many are struggling and using stock art which I don't like.Work with the background color. Make it more playful--pastels--less formal. Be creative!

Do not wait till that last day of the contest to submit. I might take the first design I like and proceed. The sooner you post a design, the better direction I can give you.
Updates

Reason: Not getting any designs I can work with yet. Please give me ideas.

All, Please re-read the brief. I have changed the banner project. It will be much easier but I need it quickly.

Now that I have made this banner much easier, I would like to wrap this contest up. Don't wait till the last day to post designs. The first design I like I will go with and close the project. Be creative, colorful, imaginative! Good luck. Martin Orvane Kelto Mobile Apps, LLC morvane@

All. See the vector file that I just purchased for the background image. Can you try different background colors. I still need the other content showing the percentages of loyalty. I do not want the rocket ship!

All, I have updated the brief. I have included a vector file that has a perfect restaurant scene. Please be creative and work with colors in this scene. Also be creative with the information in the circles showing the metrics of loyalty. Do not use the Rocket. If you find another idea to replace the rocket, that's fine. Or, just leave it off. Please make this banner unique!

Target Market(s)

Hospitality Industry.

Industry/Entity Type

Restaurant

Requirements
Must have
• Banner should be beautiful.. Image of diners at restaurant along with the statistics and message "Boost Sales".
Nice to have
• Our banner should convey the same message as the attached but we must re-design because the attached banner belongs to another company.
Should not have
• Do not re-use any of the images in the attached banner. This is from my competitor. Do not use a rocket for "Boost Sales" image.

```html
<!DOCTYPE html>
<html lang="en">
<head>
<meta charset="utf-8">
<title>KeltoPerks Loyalty Banner</title>
<link rel="stylesheet" href="https://fonts.googleapis.com/css2?family=Montserrat:wght@400;500;600;700&family=PT+Serif&display=swap">
<style>
  :root {
    --ring-red: #e8402f;
    --accent-red: #e23a2a;
    --icon-orange: #ef5a2b;
    --disc-white: #ffffff;
    --label-grey: #555555;
    --body-dark: #333333;
    --pastel-peach: #fbd9c4;
    --pastel-pink: #f7c6cf;
    --pastel-mint: #cdebdc;
    --pastel-butter: #fcefc4;
    --pastel-sky: #cfe3f3;
    --brand-ink: #3b3f5c;
  }
  html, body {
    margin: 0;
    padding: 0;
    overflow: hidden;
    background: #ffffff;
  }
  .banner {
    position: relative;
    width: 1200px;
    height: 332px;
    overflow: hidden;
    font-family: "Montserrat", Arial, sans-serif;
  }
  .banner__scene {
    position: absolute;
    inset: 0;
    background:
      radial-gradient(circle at 12% 80%, var(--pastel-mint) 0%, transparent 45%),
      radial-gradient(circle at 88% 25%, var(--pastel-sky) 0%, transparent 45%),
      radial-gradient(circle at 55% 10%, var(--pastel-butter) 0%, transparent 50%),
      linear-gradient(100deg, var(--pastel-pink) 0%, var(--pastel-peach) 45%, var(--pastel-pink) 100%);
  }
  .pitch {
    position: absolute;
    left: 36px;
    top: 112px;
    width: 210px;
    color: var(--brand-ink);
  }
  .brand {
    display: flex;
    align-items: center;
    gap: 8px;
    font-size: 17px;
    font-weight: 600;
    color: var(--brand-ink);
  }
  .brand__dot {
    width: 14px;
    height: 14px;
    border-radius: 50%;
    background: var(--ring-red);
  }
  .pitch__headline {
    margin: 12px 0 0;
    font-size: 34px;
    line-height: 1.05;
    font-weight: 700;
    color: var(--accent-red);
  }
  .stat {
    position: absolute;
    width: 196px;
    height: 196px;
    border-radius: 50%;
    background: var(--disc-white);
    border: 6px solid var(--ring-red);
    display: flex;
    flex-direction: column;
    align-items: center;
    justify-content: center;
    text-align: center;
    color: var(--body-dark);
  }
  .stat--visits { left: 266px; top: 60px; }
  .stat--spend  { left: 496px; top: 66px; }
  .stat--worth  { left: 726px; top: 64px; }
  .stat__label {
    font-size: 11px;
    font-weight: 500;
    color: var(--label-grey);
    text-transform: uppercase;
  }
  .stat__about {
    font-size: 16px;
    font-weight: 500;
    color: var(--label-grey);
    text-transform: uppercase;
    margin-top: 2px;
  }
  .stat__figure {
    font-family: "PT Serif", "Times New Roman", serif;
    font-size: 42px;
    line-height: 1;
    color: var(--accent-red);
    margin: 8px 0 6px;
  }
  .stat__compare {
    font-size: 11px;
    font-weight: 600;
    text-transform: uppercase;
  }
  .stat__base {
    font-size: 13px;
    margin-top: 3px;
  }
  .stat__icons {
    display: flex;
    align-items: center;
    gap: 8px;
    margin-top: 14px;
  }
  .stat__equation {
    font-size: 11px;
    font-weight: 500;
    margin-top: 18px;
  }
  .stat__equation--second {
    font-size: 13px;
    margin-top: 3px;
  }
  .num { color: var(--accent-red); }
</style>
</head>
<body>
  <div class="banner">
    <div class="banner__scene" role="img" aria-label="Pastel illustrated restaurant scene with guests dining at tables"></div>

    <div class="pitch">
      <div class="brand"><span class="brand__dot"></span>KeltoPerks</div>
      <h1 class="pitch__headline">Boost Sales</h1>
    </div>

    <div class="stat stat--visits">
      <div class="stat__label">Loyal guests visit</div>
      <div class="stat__about">About</div>
      <div class="stat__figure">32%</div>
      <div class="stat__compare">More than</div>
      <div class="stat__base">Average guests</div>
    </div>

    <div class="stat stat--spend">
      <div class="stat__label">Loyal guests spend</div>
      <div class="stat__about">About</div>
      <div class="stat__figure">25%</div>
      <div class="stat__compare">More than</div>
      <div class="stat__base">Average guests</div>
    </div>

    <div class="stat stat--worth">
      <div class="stat__icons">
        <svg width="40" height="46" viewBox="0 0 40 46" role="img" aria-label="One guest">
          <circle cx="20" cy="12" r="10" fill="var(--icon-orange)"/>
          <path d="M2 46 Q2 26 20 26 Q38 26 38 46 Z" fill="var(--icon-orange)"/>
        </svg>
        <svg width="14" height="14" viewBox="0 0 14 14" aria-hidden="true">
          <polyline points="2,2 6,7 2,12" fill="none" stroke="#999" stroke-width="1.2"/>
          <polyline points="7,2 11,7 7,12" fill="none" stroke="#999" stroke-width="1.2"/>
        </svg>
        <svg width="70" height="44" viewBox="0 0 70 44" role="img" aria-label="A group of guests">
          <circle cx="15" cy="14" r="8" fill="var(--icon-orange)"/>
          <path d="M1 44 Q1 26 15 26 Q29 26 29 44 Z" fill="var(--icon-orange)"/>
          <circle cx="55" cy="14" r="8" fill="var(--icon-orange)"/>
          <path d="M41 44 Q41 26 55 26 Q69 26 69 44 Z" fill="var(--icon-orange)"/>
          <circle cx="35" cy="11" r="10" fill="var(--icon-orange)" stroke="#fff" stroke-width="2"/>
          <path d="M17 44 Q17 23 35 23 Q53 23 53 44 Z" fill="var(--icon-orange)" stroke="#fff" stroke-width="2"/>
        </svg>
      </div>
      <div class="stat__equation">Loyal Guest = <span class="num">1</span></div>
      <div class="stat__equation stat__equation--second">Average Guest <span class="num">10</span></div>
    </div>
  </div>
</body>
</html>
```